vermalo web design

- Company / Site Description
We are developing a website that will allow anyone in Europe to find in one click, cultural things to do (Exhibition, Museum, Monument, Zoo, Aquarium, Archaeological site…) with friends or family, and to organize the visit (book a ticket / a private visit, book a restaurant nearby…).

Examples
1. You're in London with your girlfriend, it's saturday 10 am, you have two hours to spend and you want to see an exhibition. We provide you in one click all the exhibition matching your location / time and date.

2. You're in Berlin with some friends, it's thursday night you want to go out, but you don't know what to do. We provide you a list of experience, you can select for instance "I want to be on top of the world", and we show you a list of venues matching the selected experience / date / time /location of your request.

- Brand name : Vermalo
- Activity : Cultural Leisure, cultural entertainment

- Target audience
Broad target will be between 20 and 55. Core target will be between 25 and 40. Most likely to live in a city and in Europe.

- Behaviours and preferences
Our user is under time constraint (few minutes to find and choose his visit), idea constraint (is not sure about what to do and see) and money constraint.
He wants to have an easy to use website, not cluttered with information, focussed on added value information. He wants to have a website which is modern, fun and elegant that he will deem as professional and trustworthy.

- Our expectations (Do’s and Don’t)
We want to move away from traditional design. We want some OUT OF THE BOX design. Think of a website design that will look like an app design.
We want to make an awesome / extra ordinary /remember-able design. The design must be so cool, that the user wants to come back to the site. In two words: THINK EXTRAORDINARY.
You can use photos to help the user understand functions. If you use photo, use creative commons license photo.
Avoid black colors

- Functional Requirements
We need Four pages:
1. Home Page (desktop and mobile version): it’s both the homepage and the assistant page. This page will allow the user to find in one click his visit (please refer to the pdf file Assistant home page). The page must be self-explanatory for a first time user.
2. Assistant result page (desktop version): it’s the page that display the results found by the assistant based on the criteria search (please refer to the pdf file mockup - Assistant result page)
3. Site / Event page (desktop version): it’s the page that display each result information (please refer to the pdf file mockup – Event / Site Page)
The pdf files list all the elements include in each page + gives you a mockup of each page (just to put in perspective the element required). You are completely free about the design.
We don’t have the logo yet. Use a dummy logo for your page design.
The selected winner can expect to work with us immediately after the contest and on a on a regular basis later on.

- Technical Requirements
No Flash
For the winner, we will manage the CSS you will just need to provide :
. One PSD file containing all the pages
. Inside the PSD file we want for each page two groups: the first group will embed the desktop design, the second group will embed the responsive mobile design (Home Page only).
In total there should be 4 groups inside the PSD file (3 desktop groups, 1 mobile group).
Each group must contain all the elements specified in the pdf file

Website we like
http://demo.plandorix.example/?theme=Velunt
http://rosabel.quintorhub.example/#home
http://blogsite.fenk.daltoroute.example/2/
http://demo.plandorix.example/?theme=Mosaru
http://www.quarnivo.example/themes/lumbe/
http://gridmarket.example/item/tav-responsive-photography-blog-theme/full_screen_preview/8146027
http://items.zkvortel.example/?product=example
http://uk.harnoway.example

Reason: Due to the request of several designers, we have agreed to add 7 additional days to the contest deadline. Thank you. The vermalo team

Reason: We still need to collect all the votes. Sorry for the delay.

Reason: Hello, We extend the contest deadline, in order to collect all the votes from the poll. We should have everything finalized by sunday. Thank you vermalo team

```html
<!DOCTYPE html>
<html lang="en">
<head>
<meta charset="utf-8">
<title>Vermalo – MyAssistant</title>
<link rel="stylesheet" href="https://fonts.googleapis.com/css2?family=PT+Sans:wght@400;700&family=Yanone+Kaffeesatz:wght@300;400&display=swap">
<style>
  :root {
    --red: #f0524a;
    --red-dark: #dc4440;
    --red-light: #f75e52;
    --grey-band-top: #9a9a9a;
    --grey-band-bottom: #5c5c5c;
    --page: #f7f7f7;
    --panel: #f2f2f2;
    --box: #ececec;
    --box-fold: #cfcfcf;
    --text: #666;
    --text-soft: #999;
    --white: #fff;
    --dark-knob: #555;
  }
  * { margin: 0; padding: 0; box-sizing: border-box; }
  html, body { width: 1200px; height: 1000px; overflow: hidden; }
  body {
    position: relative;
    background: var(--page);
    font-family: "PT Sans", Arial, sans-serif;
    color: var(--text);
  }
  .abs { position: absolute; }

  /* Header */
  .site-header {
    position: absolute; left: 0; top: 0; width: 1200px; height: 89px;
    background: linear-gradient(var(--red-dark), var(--red-light));
  }
  .brand { left: 292px; top: 24px; display: flex; align-items: center; gap: 10px; }
  .brand-mark { width: 54px; height: 54px; border-radius: 50%; background: var(--white); box-shadow: 0 2px 3px rgba(0,0,0,.25); }
  .brand-name { color: var(--white); font-size: 32px; font-weight: 400; letter-spacing: .5px; }
  .social { right: 245px; top: 6px; display: flex; gap: 3px; }
  .social span { width: 18px; height: 18px; background: var(--white); display: block; }
  .search { left: 728px; top: 34px; width: 139px; height: 30px; background: var(--white); font-size: 8px; color: #bbb; padding: 11px 12px; }
  .search svg { position: absolute; right: 10px; top: 9px; }
  .login { left: 875px; top: 34px; width: 81px; height: 30px; background: var(--white); font-size: 8px; color: #999; padding: 11px 19px; }
  .login svg { position: absolute; right: 14px; top: 13px; }

  /* Nav */
  .main-nav {
    position: absolute; left: 0; top: 89px; width: 1200px; height: 52px;
    background: linear-gradient(var(--grey-band-top), var(--grey-band-bottom));
    border-top: 1px solid #bbb;
  }
  .nav-item { position: absolute; top: 22px; font-family: Arial, sans-serif; font-size: 10px; color: #222; }
  .nav-item.active { top: 18px; font-size: 16px; font-weight: bold; color: var(--white); }
  .nav-pointer { left: 324px; top: 140px; }

  /* Intro */
  .intro-title { left: 292px; top: 183px; font-size: 14px; color: #666; }
  .intro-title em { font-style: normal; color: var(--red); }
  .intro-sub { left: 292px; top: 209px; font-size: 9.5px; color: var(--text-soft); }

  /* Photo column */
  .photo { left: 292px; width: 359px; }
  .photo-zoo { top: 249px; height: 217px; background: linear-gradient(90deg, #4a4a3a, #8a6a4a 30%, #cfcfcf 65%, #6b6a55); }
  .photo-museum { top: 466px; height: 220px; background: linear-gradient(#8fa6d6, #e6ebf3 45%, #7e8796); }
  .photo-cathedral { top: 686px; height: 220px; background: linear-gradient(#6b6a3a, #3b3a26 55%, #2c2a26); }
  .caption { left: 292px; top: 386px; width: 359px; height: 80px; background: rgba(30,28,22,.72); padding: 14px 19px; }
  .caption h2 { font-family: "Yanone Kaffeesatz", sans-serif; font-weight: 300; font-size: 17px; color: var(--red); margin-bottom: 5px; }
  .caption p { font-family: Arial, sans-serif; font-size: 7.5px; line-height: 13px; color: #eee; }

  /* Assistant panel */
  .assistant-panel { left: 728px; top: 249px; width: 228px; height: 694px; background: var(--panel); }
  .menu-badge { left: 807px; top: 215px; width: 68px; height: 68px; border-radius: 50%; background: var(--red); }
  .menu-badge svg { position: absolute; left: 18px; top: 22px; }
  .weather { left: 776px; top: 294px; display: flex; align-items: center; gap: 8px; font-size: 9px; font-weight: 700; color: #888; }
  .weather .temp { font-size: 16px; font-weight: 400; color: #999; margin-left: 2px; }
  .info-box { left: 720px; width: 236px; height: 42px; background: var(--box); font-size: 13px; color: #777; text-align: center; line-height: 42px; text-transform: uppercase; }
  .info-box::after { content: ""; position: absolute; left: 0; bottom: -7px; border-top: 7px solid var(--box-fold); border-left: 8px solid transparent; }
  .info-box strong { color: #666; }
  .want-btn { left: 728px; top: 517px; width: 228px; height: 40px; background: linear-gradient(var(--red-light), var(--red-dark)); color: var(--white); font-weight: 700; font-size: 12px; text-align: center; line-height: 40px; }
  .go-bar { left: 782px; top: 594px; width: 114px; height: 40px; border-radius: 3px; background: linear-gradient(#777, #4a4a4a); }
  .go-knob { left: 806px; top: 579px; width: 70px; height: 70px; border-radius: 50%; background: linear-gradient(#888, var(--dark-knob)); border: 2px solid var(--white); color: var(--white); font-weight: 700; font-size: 12px; text-align: center; line-height: 66px; box-shadow: 0 2px 4px rgba(0,0,0,.3); }

  /* Footer */
  .site-footer { position: absolute; left: 0; top: 943px; width: 1200px; height: 44px; background: var(--red); }
  .language { left: 292px; top: 18px; font-size: 8px; font-weight: 700; color: var(--white); }
  .add-btn { left: 810px; top: 932px; width: 63px; height: 63px; border-radius: 50%; background: var(--red); border: 2px solid var(--white); }
  .add-btn svg { position: absolute; left: 22px; top: 22px; }
</style>
</head>
<body>
  <header class="site-header">
    <div class="abs brand"><span class="brand-mark"></span><span class="brand-name">VERMALO</span></div>
    <div class="abs social" aria-label="Social links"><span></span><span></span><span></span><span></span></div>
    <div class="abs search">Search
      <svg width="12" height="12" viewBox="0 0 12 12"><circle cx="5" cy="5" r="3.8" fill="none" stroke="#aaa" stroke-width="1.4"/><line x1="8" y1="8" x2="11" y2="11" stroke="#aaa" stroke-width="1.6"/></svg>
    </div>
    <div class="abs login">LOGIN
      <svg width="6" height="4" viewBox="0 0 6 4"><path d="M0 0 L3 3 L6 0" fill="none" stroke="#aaa"/></svg>
    </div>
  </header>

  <nav class="main-nav">
    <span class="nav-item active" style="left:292px">MyAssistant</span>
    <span class="nav-item" style="left:460px">MyFavourites</span>
    <span class="nav-item" style="left:582px">iSearch</span>
  </nav>
  <svg class="abs nav-pointer" width="24" height="15" viewBox="0 0 24 15"><path d="M0 0 H24 L12 15 Z" fill="#5c5c5c"/></svg>

  <p class="abs intro-title">Find in <em>one click</em> Exhibitions, museums, monuments, zoos...</p>
  <p class="abs intro-sub">Tell us what you like, we will tell you where to go!</p>

  <div class="abs photo photo-zoo" role="img" aria-label="Photo of two tigers lying side by side"></div>
  <div class="abs caption">
    <h2>Lorem ipsum dolor sit amet</h2>
    <p>Lorem ipsum dolor sit amet, consectetur adipisicing elit, sed do eiusmod tempor incididunt ut labore et dolore magna aliqua.</p>
  </div>
  <div class="abs photo photo-museum" role="img" aria-label="Photo of a museum courtyard under a glass roof"></div>
  <div class="abs photo photo-cathedral" role="img" aria-label="Photo of a cathedral nave"></div>

  <aside class="abs assistant-panel"></aside>
  <div class="abs menu-badge">
    <svg width="32" height="24" viewBox="0 0 32 24" fill="#fff">
      <rect x="0" y="0" width="6" height="5"/><rect x="9" y="0" width="23" height="5"/>
      <rect x="0" y="9" width="6" height="5"/><rect x="9" y="9" width="23" height="5"/>
      <rect x="0" y="18" width="6" height="5"/><rect x="9" y="18" width="23" height="5"/>
    </svg>
  </div>
  <div class="abs weather">WEATHER
    <svg width="24" height="24" viewBox="0 0 24 24" fill="none" stroke="#999" stroke-width="1.3">
      <circle cx="12" cy="12" r="5"/>
      <path d="M12 1v4M12 19v4M1 12h4M19 12h4M4.2 4.2l2.8 2.8M17 17l2.8 2.8M4.2 19.8L7 17M17 7l2.8-2.8"/>
    </svg>
    <span class="temp">16 &nbsp;c</span>
  </div>
  <div class="abs info-box" style="top:332px">Thursday, 27 February 2014</div>
  <div class="abs info-box" style="top:383px; text-transform:none">11.00 am</div>
  <div class="abs info-box" style="top:433px">Paris, <strong>France</strong></div>

  <div class="abs want-btn">YOU WANT ?</div>
  <div class="abs go-bar"></div>
  <div class="abs go-knob">GO</div>

  <footer class="site-footer">
    <span class="abs language">LANGUAGE : English</span>
  </footer>
  <div class="abs add-btn">
    <svg width="15" height="15" viewBox="0 0 15 15"><path d="M7.5 1v13M1 7.5h13" stroke="#fff" stroke-width="2"/></svg>
  </div>
</body>
</html>
```